Criação de Papelaria Profissional para Limpeza & Serviço para o lar
" Nossa empresa e familiar, buscamos fazer nosso trabalho com excelencia e qualidade visando o bem estar de nossos clientes. "

```html
<!DOCTYPE html>
<html lang="en">
<head>
<meta charset="utf-8">
<title>TidyNest Cleaning LLC – Business Cards</title>
<link rel="stylesheet" href="https://fonts.googleapis.com/css2?family=Poppins:wght@300;700&display=swap">
<style>
  :root {
    --bg: #e4e6e5;
    --card-white: #ffffff;
    --brand-teal: #4fbf98;
    --brand-copper: #c7813e;
    --ink-light: #ffffff;
    --shadow: rgba(40, 50, 48, 0.18);
  }
  * { box-sizing: border-box; margin: 0; padding: 0; }
  html, body {
    width: 1200px;
    height: 1200px;
    overflow: hidden;
    background: var(--bg);
    font-family: "Poppins", sans-serif;
  }
  .sheet {
    width: 1200px;
    height: 1200px;
    display: flex;
    flex-direction: column;
    align-items: center;
    justify-content: center;
    gap: 60px;
  }
  .card {
    width: 840px;
    height: 480px;
    border-radius: 36px;
    position: relative;
    box-shadow: 0 14px 36px var(--shadow);
    overflow: hidden;
  }
  .card--front { background: var(--card-white); }
  .card--back { background: var(--brand-teal); }

  .brand {
    position: absolute;
    display: flex;
    align-items: center;
    gap: 18px;
  }
  .brand__dot {
    width: 64px;
    height: 64px;
    border-radius: 50%;
    background: var(--brand-copper);
    flex-shrink: 0;
  }
  .brand__name {
    font-weight: 700;
    font-size: 46px;
    line-height: 1.05;
    letter-spacing: -0.5px;
  }
  .card--front .brand { right: 64px; top: 50%; transform: translateY(-50%); }
  .card--front .brand__name { color: var(--brand-teal); }

  .card--back .brand { right: 72px; top: 110px; }
  .card--back .brand__name { color: var(--ink-light); font-size: 28px; }
  .card--back .brand__dot { width: 72px; height: 72px; }

  .contact {
    position: absolute;
    left: 60px;
    top: 250px;
    list-style: none;
    color: var(--ink-light);
    font-weight: 300;
    font-size: 24px;
    line-height: 1.55;
  }
</style>
</head>
<body>
  <main class="sheet">
    <section class="card card--front">
      <div class="brand">
        <span class="brand__dot"></span>
        <span class="brand__name">TidyNest<br>Cleaning LLC</span>
      </div>
    </section>

    <section class="card card--back">
      <ul class="contact">
        <li>(00) 90000-1234</li>
        <li>@tidynestcleaning</li>
        <li>hello@tidynestcleaning.com</li>
      </ul>
      <div class="brand">
        <span class="brand__dot"></span>
        <span class="brand__name">TidyNest</span>
      </div>
    </section>
  </main>
</body>
</html>
```